依頼詳細
ホームページ自体は少し前のものとなっており、今風のまた将来性の有るイメージを訴求できるデザインにリニューアルしたいと考えております。
WEBマーケティングとSEO対策を取り入れ、コンテンツの改善をおこなっていきます。
企業のイメージとしましては、あ母さんのぬくもり、やさしさ、女性のあたたかいこころ(母性)を感じられるようなイメージを重視しておりますので、ホームページの全体の雰囲気やデザインの際に取り入れていただきたいと思います。
サイトURL
http://mekutorin.co.jp
ページ数
1ページ
希望イメージ
シンプル 複雑
単色 カラフル
暗い 明るい
日常 高級
遊び心 厳粛
未来的 伝統的
女性的 男性的
希望する色
赤系、緑系、黄・オレンジ系
納品ファイル
• 高解像度JPG (.jpg)
• イラストレーター形式 (.ai)
• フォトショップ形式 (.psd)
補足説明
ロゴデータはないため店舗の画像データから流用いただければと思います。
添付の画像以外のコインランドリーイメージ等はインタネット上の有料画像素材等をご利用下さい。実際に採用の際に画像を購入させていただきます。
お世話になっております。
デザイン指示書を更新いたします。
ご確認よろしくお願いいたします。
■ 選んだ理由

お客様に雰囲気がとても良く良いデザインありがとうございます。
とのことです。
簡単な修正等も有りますのでご対応よろしくお願いいたします。

■ 提案者全員のお礼・コメント

素晴らしいデザインありがとうございました。今後もデザインコンペを行ってまいりますのでよろしくお願いいたします。

```html
<!DOCTYPE html>
<html lang="ja">
<head>
<meta charset="utf-8">
<title>ひだまりランドリー コインランドリーフランチャイズ</title>
<link href="https://fonts.googleapis.com/css2?family=M+PLUS+Rounded+1c:wght@400;700;800&family=Noto+Sans+JP:wght@400;700&display=swap" rel="stylesheet">
<style>
:root{
  --orange:#f39a1e;
  --orange-dark:#e07d00;
  --yellow:#fcd86a;
  --cream:#fbf4e4;
  --beige:#efe3c8;
  --teal:#35b4c6;
  --teal-light:#e4f5f8;
  --green:#8cc63f;
  --brown:#5a3d22;
  --text:#555;
  --grey:#f2f2f2;
  --line:#dedede;
  --dark:#3b3b3b;
}
*{box-sizing:border-box;margin:0;padding:0}
html,body{width:1200px;height:2936px;overflow:hidden}
body{font-family:"Noto Sans JP",sans-serif;color:var(--text);background:#fff;font-size:13px;position:relative}
.wrap{width:1000px;margin:0 auto;position:relative}
.round{font-family:"M PLUS Rounded 1c",sans-serif}

/* header */
.site-header{height:120px}
.site-header .wrap{display:flex;justify-content:space-between;align-items:center;height:120px}
.brand{display:flex;align-items:center;gap:10px}
.brand-dot{width:18px;height:18px;border-radius:50%;background:var(--orange)}
.brand-name{font-family:"M PLUS Rounded 1c",sans-serif;font-weight:800;font-size:34px;color:var(--orange)}
.brand-sub{font-size:11px;color:#888;margin-top:4px}
.contact{display:flex;align-items:center;gap:14px}
.contact-note{font-size:11px;color:#777;text-align:right;line-height:1.6}
.contact-icon{width:46px;height:46px;border-radius:50%;background:var(--orange);display:flex;align-items:center;justify-content:center}
.contact-tel small{display:block;font-size:12px;color:var(--orange);font-weight:700}
.contact-tel b{font-size:32px;color:var(--brown);font-family:"M PLUS Rounded 1c",sans-serif;font-weight:800;letter-spacing:1px}

/* nav */
.global-nav{height:50px;border-top:1px solid var(--line);border-bottom:1px solid var(--line);background:#fff}
.global-nav ul{list-style:none;display:flex;justify-content:center;height:48px}
.global-nav li{width:130px;display:flex;align-items:center;justify-content:center;font-size:13px;color:#666;border-right:1px solid var(--line)}
.global-nav li:first-child{border-left:1px solid var(--line);background:var(--grey);color:var(--orange);font-weight:700}

/* hero */
.hero{height:480px;position:relative;background:linear-gradient(180deg,#dfe8ef 0%,#eef1f3 55%,#cfcfcf 56%,#b9b9b9 100%)}
.hero-photo{position:absolute;inset:0;background:linear-gradient(100deg,#c9d6de 0%,#e8ecef 40%,#d8d2c6 70%,#bdb6a8 100%)}
.hero-copy{position:absolute;left:100px;top:150px;width:520px;background:rgba(255,255,255,.82);padding:26px 30px;border-left:8px solid var(--orange)}
.hero-copy .kicker{font-size:14px;color:var(--orange);font-weight:700}
.hero-copy h1{font-family:"M PLUS Rounded 1c",sans-serif;font-weight:800;font-size:38px;line-height:1.35;color:var(--brown);margin:6px 0 10px}
.hero-copy h1 em{font-style:normal;color:var(--orange)}
.hero-copy p{font-size:13px}
.hero-cta{position:absolute;right:120px;top:260px;width:230px;height:90px;background:var(--orange);border-radius:10px;color:#fff;display:flex;flex-direction:column;justify-content:center;padding-left:26px;font-family:"M PLUS Rounded 1c",sans-serif;font-weight:700;font-size:18px;line-height:1.4;box-shadow:0 4px 0 var(--orange-dark)}
.hero-cta small{font-size:14px;color:var(--yellow)}

/* two columns */
.columns{display:flex;gap:40px;margin-top:40px;height:1150px}
.main{width:700px}
.side{width:260px}
.sec-title{font-family:"M PLUS Rounded 1c",sans-serif;font-weight:800;font-size:18px;color:var(--brown);border-left:6px solid var(--orange);padding-left:12px;height:30px;display:flex;align-items:center;border-bottom:1px dashed var(--line)}
.intro p{font-size:12.5px;line-height:2;margin:14px 0 0}
.news{margin-top:28px}
.news ul{list-style:none;margin-top:6px}
.news li{display:flex;height:42px;align-items:center;border-bottom:1px dotted #ccc;font-size:12.5px}
.news time{width:110px;color:#888}

.voices{margin-top:40px}
.voice-list{display:flex;gap:12px;margin-top:14px;padding:14px;background:var(--beige)}
.voice{flex:1;height:170px;background:var(--orange);border-radius:6px;color:#fff;padding:12px;text-align:center}
.voice h3{font-size:13px;font-weight:700;border-bottom:1px dashed rgba(255,255,255,.6);padding-bottom:6px}
.voice p{font-size:11px;line-height:1.7;margin-top:8px;text-align:left}
.voice-person{width:44px;height:44px;border-radius:50%;background:rgba(255,255,255,.35);margin:10px auto 0}

.merit{margin-top:30px;background:var(--beige);padding:16px;height:400px;border-radius:6px}
.merit-head{height:66px;background:var(--teal);border-radius:34px;display:flex;align-items:center;justify-content:center;gap:14px;color:#fff;font-family:"M PLUS Rounded 1c",sans-serif;font-weight:800;font-size:24px}
.merit-head span{width:40px;height:40px;border-radius:50%;background:var(--yellow)}
.merit-body{display:flex;gap:20px;margin-top:20px}
.merit-col{flex:1;background:#fff;border-radius:6px;padding:14px}
.merit-col h3{font-family:"M PLUS Rounded 1c",sans-serif;font-size:16px;font-weight:800;margin-bottom:10px}
.merit-col.good h3{color:var(--orange)}
.merit-col.bad h3{color:var(--teal)}
.pill{height:34px;border-radius:17px;display:flex;align-items:center;padding-left:16px;font-size:11.5px;color:#fff;margin-bottom:10px}
.good .pill{background:var(--orange)}
.bad .pill{background:var(--teal)}

/* sidebar */
.banner{display:flex;flex-direction:column;justify-content:center;padding:0 18px;border-radius:4px;color:#fff;font-family:"M PLUS Rounded 1c",sans-serif;font-weight:800;margin-bottom:18px}
.banner small{font-size:13px;font-weight:700}
.banner.land{height:120px;background:var(--green);font-size:22px}
.banner.owner{height:100px;background:var(--orange);font-size:24px}
.banner.faq{height:80px;background:var(--grey);color:var(--brown);font-size:18px;flex-direction:row;align-items:center;gap:12px;justify-content:flex-start}
.faq-mark{width:44px;height:44px;border-radius:50%;background:var(--orange);color:#fff;display:flex;align-items:center;justify-content:center;font-size:14px}
.company{margin-top:80px}
.company-map{height:110px;background:linear-gradient(135deg,#e6e6e6,#d2d2d2);margin-top:12px}
.office{text-align:center;font-size:11.5px;line-height:1.8;padding:12px 0;border-bottom:1px dotted #ccc}
.office b{display:block;font-size:13px;color:var(--brown)}
.mini-banner{height:70px;border:2px solid var(--orange);border-radius:6px;display:flex;align-items:center;gap:12px;padding-left:16px;margin-top:16px;font-weight:700;color:var(--orange);font-size:15px}
.mini-banner i{width:38px;height:38px;border-radius:4px;background:var(--orange);display:block}

/* comparison */
.compare{margin-top:20px}
.compare-box{border-radius:8px;padding:0 30px 24px;position:relative}
.compare-box h2{margin:0 auto;width:360px;height:40px;border-radius:0 0 20px 20px;display:flex;align-items:center;justify-content:center;color:#fff;font-family:"M PLUS Rounded 1c",sans-serif;font-weight:800;font-size:17px}
.compare-box.other{background:var(--grey);height:190px}
.compare-box.other h2{background:#9a9a9a}
.compare-box.ours{background:var(--teal-light);height:220px;border:2px solid var(--teal)}
.compare-box.ours h2{background:var(--orange)}
.compare-inner{display:flex;gap:30px;margin-top:22px}
.compare-img{width:220px;height:110px;border-radius:4px;flex:none}
.other .compare-img{background:linear-gradient(135deg,#cfd5d8,#aab3b8)}
.ours .compare-img{background:linear-gradient(135deg,#ffe3b0,#9fdbe3);height:130px}
.compare-inner p{font-size:12.5px;line-height:2}
.arrow{height:40px;display:flex;justify-content:center;align-items:center}

/* recommend */
.recommend{margin-top:40px}
.recommend h2{height:64px;background:var(--yellow);border-radius:32px;display:flex;align-items:center;justify-content:center;font-family:"M PLUS Rounded 1c",sans-serif;font-weight:800;font-size:22px;color:var(--brown);width:640px;margin:0 auto}
.recommend p{font-size:12.5px;line-height:2.1;margin-top:22px}

/* footer */
.footer-nav{position:absolute;left:0;top:2848px;width:1200px;height:40px;background:var(--orange)}
.footer-nav ul{list-style:none;display:flex;justify-content:center;height:40px}
.footer-nav li{color:#fff;font-size:12px;padding:0 26px;display:flex;align-items:center;border-right:1px solid rgba(255,255,255,.5)}
.footer-nav li:first-child{border-left:1px solid rgba(255,255,255,.5)}
.copyright{position:absolute;left:0;top:2888px;width:1200px;height:48px;background:var(--dark);color:#ccc;font-size:11px;display:flex;align-items:center;justify-content:center}
</style>
</head>
<body>

<header class="site-header">
  <div class="wrap">
    <div>
      <div class="brand"><span class="brand-dot"></span><span class="brand-name">ひだまりランドリー</span></div>
      <p class="brand-sub">コインランドリーフランチャイズ 有限会社ひだまりランドリー</p>
    </div>
    <div class="contact">
      <p class="contact-note">受付時間 平日9:00〜18:00<br>コインランドリー経営の相談受付中</p>
      <div class="contact-icon">
        <svg width="24" height="24" viewBox="0 0 24 24"><path fill="#fff" d="M6.6 10.8a15 15 0 006.6 6.6l2.2-2.2c.3-.3.7-.4 1-.2 1.1.4 2.3.6 3.6.6.6 0 1 .4 1 1V20c0 .6-.4 1-1 1A17 17 0 013 4c0-.6.4-1 1-1h3.5c.6 0 1 .4 1 1 0 1.3.2 2.5.6 3.6.1.3 0 .7-.2 1z"/></svg>
      </div>
      <div class="contact-tel"><small>お気軽にお電話下さい！</small><b>0120-000-123</b></div>
    </div>
  </div>
</header>

<nav class="global-nav">
  <ul>
    <li>HOME</li><li>FCについて</li><li>店舗の紹介</li><li>資料</li><li>ご利用の流れ</li><li>会社概要</li>
  </ul>
</nav>

<section class="hero">
  <div class="hero-photo" role="img" aria-label="晴れた日の郊外にあるコインランドリー店舗と駐車場の写真"></div>
  <div class="hero-copy">
    <p class="kicker">コインランドリー</p>
    <h1>長期安定収入を<br><em>コインランドリー経営</em>で実現！</h1>
    <p>コインランドリー経営のことならお気軽にご相談ください。</p>
  </div>
  <div class="hero-cta"><span>フランチャイズ</span><small>資料請求はコチラ ›</small></div>
</section>

<div class="wrap">
  <div class="columns">
    <div class="main">
      <section class="intro">
        <h2 class="sec-title">ひだまりランドリーのこだわり</h2>
        <p>清潔で明るい店内づくりを大切にし、地域の皆さまが安心してご利用いただけるお店を目指しています。オーナー様には開業前の立地調査から運営のサポートまで、一つひとつ丁寧に寄り添います。家族のように温かい関係を築き、長く続く安定した経営をお手伝いいたします。お気軽にご相談ください。</p>
      </section>

      <section class="news">
        <h2 class="sec-title">新着情報</h2>
        <ul>
          <li><time>2017.01.20</time>新店舗のオープン情報を掲載いたしました。</li>
          <li><time>2017.01.20</time>オーナー様向け説明会の日程を更新しました。</li>
          <li><time>2017.01.20</time>年末年始の営業時間についてのお知らせ。</li>
          <li><time>2017.01.20</time>ホームページをリニューアルいたしました。</li>
          <li><time>2017.01.20</time>資料請求のお申し込みを受け付けています。</li>
        </ul>
      </section>

      <section class="voices">
        <h2 class="sec-title">コインランドリーFCオーナー様の声</h2>
        <div class="voice-list">
          <div class="voice"><h3>オーナー様の声 1</h3><p>開業まで丁寧に支えてもらえて安心でした。</p><div class="voice-person"></div></div>
          <div class="voice"><h3>オーナー様の声 2</h3><p>手間が少なく本業と両立できています。</p><div class="voice-person"></div></div>
          <div class="voice"><h3>オーナー様の声 3</h3><p>地域の方に喜ばれるお店になりました。</p><div class="voice-person"></div></div>
          <div class="voice"><h3>オーナー様の声 4</h3><p>収入が安定し将来の不安が減りました。</p><div class="voice-person"></div></div>
        </div>
      </section>

      <section class="merit">
        <h2 class="merit-head"><span></span>コインランドリーFCのメリット・デメリット<span></span></h2>
        <div class="merit-body">
          <div class="merit-col good">
            <h3>メリット</h3>
            <div class="pill">人件費がほとんどかかりません</div>
            <div class="pill">在庫を抱える必要がありません</div>
            <div class="pill">長期で安定した収入が見込めます</div>
            <div class="pill">専門知識がなくても始められます</div>
          </div>
          <div class="merit-col bad">
            <h3>デメリット</h3>
            <div class="pill">初期投資がある程度必要です</div>
            <div class="pill">立地によって売上が変わります</div>
            <div class="pill">定期的な清掃と点検が必要です</div>
            <div class="pill">収益化まで時間がかかる場合も</div>
          </div>
        </div>
      </section>
    </div>

    <aside class="side">
      <div class="banner land"><small>コインランドリー物件募集</small>地主・不動産<br>顧問会社様</div>
      <div class="banner owner"><small>コインランドリー</small>オーナー募集</div>
      <div class="banner faq"><span class="faq-mark">FAQ</span>よくあるご質問</div>

      <section class="company">
        <h2 class="sec-title">会社情報</h2>
        <div class="company-map" role="img" aria-label="本社周辺の地図"></div>
        <div class="office"><b>栃木本社</b>栃木県宇都宮市中央1-2-3<br>TEL 028-000-0001</div>
        <div class="office"><b>茨城営業所</b>茨城県水戸市桜町4-5-6<br>TEL 029-000-0002</div>
        <div class="office"><b>福島営業所</b>福島県郡山市若葉7-8-9<br>TEL 024-000-0003</div>
      </section>
      <div class="mini-banner"><i></i>資料請求</div>
      <div class="mini-banner"><i></i>お問い合わせ</div>
    </aside>
  </div>

  <section class="compare">
    <div class="compare-box other">
      <h2>その他のFCの場合</h2>
      <div class="compare-inner">
        <div class="compare-img" role="img" aria-label="一般的な店舗設備のイメージ"></div>
        <p>一般的なフランチャイズでは人材の確保や在庫管理、長時間の運営が必要となり、オーナー様の負担が大きくなりがちです。ロイヤリティの支払いも毎月発生し、利益を圧迫することがあります。</p>
      </div>
    </div>
    <div class="arrow"><svg width="60" height="30" viewBox="0 0 60 30"><path d="M0 0h60L30 30z" fill="#f39a1e"/></svg></div>
    <div class="compare-box ours">
      <h2>コインランドリーFCの場合</h2>
      <div class="compare-inner">
        <div class="compare-img" role="img" aria-label="明るく清潔なコインランドリー店舗のイメージ"></div>
        <p>コインランドリーは無人運営が可能で、人件費や在庫の心配がほとんどありません。機器の管理から集客まで本部がしっかりサポートいたしますので、初めての方でも安心して長期安定経営を目指せます。</p>
      </div>
    </div>
  </section>

  <section class="recommend">
    <h2>このような方にコインランドリー経営をススメします！</h2>
    <p>土地や建物を有効に活用したい方、本業とは別に安定した収入源をつくりたい方、将来に向けた資産運用を考えている方におすすめです。コインランドリーは天候や季節に左右されにくく、共働き世帯の増加とともに需要が高まっています。人を雇う必要が少ないため、経営の手間を抑えながら地域に役立つお店を持つことができます。開業までの流れや費用について、まずはお気軽に資料をご請求ください。担当者がオーナー様お一人おひとりに合わせたご提案をいたします。</p>
  </section>
</div>

<nav class="footer-nav">
  <ul><li>HOME</li><li>FCについて</li><li>店舗の紹介</li><li>資料</li><li>ご利用の流れ</li><li>会社概要</li></ul>
</nav>
<footer class="copyright">Copyright © 2017 ひだまりランドリー All Rights Reserved.</footer>

</body>
</html>
```